WordPress Site That Reviews Footwear

We need a wordpress web design for an affiliate site called TarnWisp. We review and do roundups on footwear products. The final design should be clean and mobile friendly. The site should be built with Gutenberg page builder. We like the design of https://petalharvin.com/.

Target Market(s)

USA

Industry/Entity Type

Footwear

Logo Text

TarnWisp

Number of Pages Required

4 page

Font styles to use
Serif
Sans Serif

Requirements
Must have
• Wordpress site
Blog post
Page
Categories
Homepage

```html
<!DOCTYPE html>
<html lang="en">
<head>
<meta charset="utf-8">
<title>TarnWisp — Blog</title>
<link rel="stylesheet" href="https://fonts.googleapis.com/css2?family=Jost:wght@300;400;500&display=swap">
<style>
  :root{
    --accent:#f2665c;
    --ink:#2c2c2c;
    --body:#5a5a5a;
    --page:#ffffff;
    --footer:#252626;
    --footer-text:#d6d6d6;
    --footer-muted:#8a8a8a;
  }
  *{margin:0;padding:0;box-sizing:border-box}
  html,body{width:944px;height:1200px;overflow:hidden;background:var(--page)}
  body{position:relative;font-family:"Jost",sans-serif;color:var(--ink)}

  .site-header{position:absolute;top:0;left:0;width:944px;height:62px}
  .brand{position:absolute;left:145px;top:22px;font-size:15px;font-weight:400;letter-spacing:2.6px;color:var(--accent)}
  .main-nav{position:absolute;top:25px;left:0;width:944px}
  .main-nav a{position:absolute;font-size:9px;font-weight:300;color:var(--ink);text-decoration:none;letter-spacing:.2px}
  .main-nav .is-active::after{content:"";position:absolute;left:50%;top:17px;width:3px;height:3px;margin-left:-1.5px;border-radius:50%;background:var(--accent)}

  .post-grid{position:absolute;left:145px;top:93px;width:654.5px;display:grid;grid-template-columns:repeat(3,206.5px);column-gap:17.5px;grid-template-rows:repeat(3,251px)}
  .post-card__media{height:139px;width:206.5px}
  .post-card__title{margin-top:11px;font-size:10.8px;line-height:14px;font-weight:400;color:var(--ink)}
  .post-card__excerpt{margin-top:2px;font-size:9px;line-height:16px;font-weight:300;color:var(--body)}
  .read-more{margin-top:9px;display:flex;align-items:center;height:14px;font-size:9.3px;color:var(--accent);text-decoration:none;font-weight:400}
  .read-more svg{margin-left:8px}

  .pagination{position:absolute;top:860px;left:0;width:944px;text-align:center}
  .pagination__count{font-size:10.5px;font-weight:400;color:var(--ink);letter-spacing:.3px}
  .pagination__pages{margin-top:6px;font-size:9.5px;display:flex;justify-content:center;align-items:center;gap:7px;padding-left:4px}
  .pagination__pages .current{color:var(--accent);position:relative}
  .pagination__pages .current::after{content:"";position:absolute;left:50%;top:16px;width:2.5px;height:2.5px;margin-left:-1px;border-radius:50%;background:var(--accent)}

  .site-footer{position:absolute;left:0;top:922px;width:944px;height:278px;background:var(--footer);color:var(--footer-text)}
  .footer-brand{position:absolute;left:145px;top:104px;font-size:14px;font-weight:400;color:#fff;letter-spacing:.3px}
  .footer-col{position:absolute;top:57px}
  .footer-col h3{font-size:9.6px;font-weight:400;color:#fff;letter-spacing:.2px;height:12px}
  .footer-col ul{list-style:none;margin-top:15px}
  .footer-col li{font-size:8.8px;font-weight:300;line-height:10px;margin-bottom:17px;display:flex;align-items:center}
  .footer-col li svg{margin-right:7px;flex:none}
  .social{display:flex;align-items:center;gap:10px;margin-top:-2px;margin-left:-1px;font-size:8.8px;font-weight:300}
  .social span.dot{width:9px;height:9px;border:1.3px solid #fff;border-radius:50%}
  .copyright{position:absolute;left:0;width:944px;top:248px;text-align:center;font-size:8.2px;font-weight:300;color:var(--footer-muted)}
  .copyright strong{color:var(--accent);font-weight:500}
</style>
</head>
<body>
  <header class="site-header">
    <div class="brand">TARNWISP</div>
    <nav class="main-nav">
      <a href="#" style="left:481px">HOME</a>
      <a href="#" style="left:545px">PAGES</a>
      <a href="#" class="is-active" style="left:609px">BLOG</a>
      <a href="#" style="left:669px">CATEGORIES</a>
      <a href="#" style="left:759px">CONTACT</a>
    </nav>
  </header>

  <main class="post-grid">
    <article class="post-card">
      <div class="post-card__media" role="img" aria-label="Runner tying a sneaker lace on a sunlit trail" style="background:linear-gradient(120deg,#3a3430,#6b5a48 55%,#d9cfae)"></div>
      <h2 class="post-card__title">Lorem ipsum dolor sit amet</h2>
      <p class="post-card__excerpt">Ut consequat, sapien at scelerisque laoreet, nulla turpis aliquet quam, quis imperdiet nulla nisl</p>
      <a class="read-more" href="#">Read More<svg width="34" height="12" viewBox="0 0 34 12"><line x1="8" y1="6" x2="34" y2="6" stroke="#f2665c" stroke-width="0.8"/><circle cx="6" cy="6" r="5.5" fill="#f2665c"/><path d="M3.8 6h4.4M6 3.8v4.4" stroke="#fff" stroke-width="1.1"/></svg></a>
    </article>
    <article class="post-card">
      <div class="post-card__media" role="img" aria-label="Leather shoes displayed on wooden crates" style="background:linear-gradient(160deg,#5b4a3c,#b08a5e 50%,#d4b482)"></div>
      <h2 class="post-card__title">Lorem ipsum dolor sit amet</h2>
      <p class="post-card__excerpt">Ut consequat, sapien at scelerisque laoreet, nulla turpis aliquet quam, quis imperdiet nulla nisl</p>
      <a class="read-more" href="#">Read More<svg width="34" height="12" viewBox="0 0 34 12"><line x1="8" y1="6" x2="34" y2="6" stroke="#f2665c" stroke-width="0.8"/><circle cx="6" cy="6" r="5.5" fill="#f2665c"/><path d="M3.8 6h4.4M6 3.8v4.4" stroke="#fff" stroke-width="1.1"/></svg></a>
    </article>
    <article class="post-card">
      <div class="post-card__media" role="img" aria-label="Shopper examining a shoe in a menswear store" style="background:linear-gradient(110deg,#2e2b2a,#7a7470 45%,#8a5a3c)"></div>
      <h2 class="post-card__title">Lorem ipsum dolor sit amet</h2>
      <p class="post-card__excerpt">Ut consequat, sapien at scelerisque laoreet, nulla turpis aliquet quam, quis imperdiet nulla nisl</p>
      <a class="read-more" href="#">Read More<svg width="34" height="12" viewBox="0 0 34 12"><line x1="8" y1="6" x2="34" y2="6" stroke="#f2665c" stroke-width="0.8"/><circle cx="6" cy="6" r="5.5" fill="#f2665c"/><path d="M3.8 6h4.4M6 3.8v4.4" stroke="#fff" stroke-width="1.1"/></svg></a>
    </article>

    <article class="post-card">
      <div class="post-card__media" role="img" aria-label="Running shoes on a gym treadmill" style="background:linear-gradient(120deg,#d99a52,#5c4a3e 40%,#2f2f33)"></div>
      <h2 class="post-card__title">Lorem ipsum dolor sit amet</h2>
      <p class="post-card__excerpt">Ut consequat, sapien at scelerisque laoreet, nulla turpis aliquet quam, quis imperdiet nulla nisl</p>
      <a class="read-more" href="#">Read More<svg width="34" height="12" viewBox="0 0 34 12"><line x1="8" y1="6" x2="34" y2="6" stroke="#f2665c" stroke-width="0.8"/><circle cx="6" cy="6" r="5.5" fill="#f2665c"/><path d="M3.8 6h4.4M6 3.8v4.4" stroke="#fff" stroke-width="1.1"/></svg></a>
    </article>
    <article class="post-card">
      <div class="post-card__media" role="img" aria-label="Brown leather boots above a calm lake at dusk" style="background:linear-gradient(180deg,#c9a07c,#6d6a72 45%,#2a2c33)"></div>
      <h2 class="post-card__title">Lorem ipsum dolor sit amet</h2>
      <p class="post-card__excerpt">Ut consequat, sapien at scelerisque laoreet, nulla turpis aliquet quam, quis imperdiet nulla nisl</p>
      <a class="read-more" href="#">Read More<svg width="34" height="12" viewBox="0 0 34 12"><line x1="8" y1="6" x2="34" y2="6" stroke="#f2665c" stroke-width="0.8"/><circle cx="6" cy="6" r="5.5" fill="#f2665c"/><path d="M3.8 6h4.4M6 3.8v4.4" stroke="#fff" stroke-width="1.1"/></svg></a>
    </article>
    <article class="post-card">
      <div class="post-card__media" role="img" aria-label="Yellow heels and handbag beside a beige sofa" style="background:linear-gradient(130deg,#3a3a3c,#8a8580 50%,#c9bfb2)"></div>
      <h2 class="post-card__title">Lorem ipsum dolor sit amet</h2>
      <p class="post-card__excerpt">Ut consequat, sapien at scelerisque laoreet, nulla turpis aliquet quam, quis imperdiet nulla nisl</p>
      <a class="read-more" href="#">Read More<svg width="34" height="12" viewBox="0 0 34 12"><line x1="8" y1="6" x2="34" y2="6" stroke="#f2665c" stroke-width="0.8"/><circle cx="6" cy="6" r="5.5" fill="#f2665c"/><path d="M3.8 6h4.4M6 3.8v4.4" stroke="#fff" stroke-width="1.1"/></svg></a>
    </article>

    <article class="post-card">
      <div class="post-card__media" role="img" aria-label="Platform sneakers and handbag on stone steps" style="background:linear-gradient(170deg,#b8c2c8,#9c958c 45%,#8a7f72)"></div>
      <h2 class="post-card__title">Lorem ipsum dolor sit amet</h2>
      <p class="post-card__excerpt">Ut consequat, sapien at scelerisque laoreet, nulla turpis aliquet quam, quis imperdiet nulla nisl</p>
      <a class="read-more" href="#">Read More<svg width="34" height="12" viewBox="0 0 34 12"><line x1="8" y1="6" x2="34" y2="6" stroke="#f2665c" stroke-width="0.8"/><circle cx="6" cy="6" r="5.5" fill="#f2665c"/><path d="M3.8 6h4.4M6 3.8v4.4" stroke="#fff" stroke-width="1.1"/></svg></a>
    </article>
    <article class="post-card">
      <div class="post-card__media" role="img" aria-label="Polishing a leather brogue in a workshop" style="background:linear-gradient(140deg,#6b4a2e,#3a2618 50%,#1c1410)"></div>
      <h2 class="post-card__title">Lorem ipsum dolor sit amet</h2>
      <p class="post-card__excerpt">Ut consequat, sapien at scelerisque laoreet, nulla turpis aliquet quam, quis imperdiet nulla nisl</p>
      <a class="read-more" href="#">Read More<svg width="34" height="12" viewBox="0 0 34 12"><line x1="8" y1="6" x2="34" y2="6" stroke="#f2665c" stroke-width="0.8"/><circle cx="6" cy="6" r="5.5" fill="#f2665c"/><path d="M3.8 6h4.4M6 3.8v4.4" stroke="#fff" stroke-width="1.1"/></svg></a>
    </article>
    <article class="post-card">
      <div class="post-card__media" role="img" aria-label="Shopper trying on heels in a bright shoe boutique" style="background:linear-gradient(120deg,#e8e4df,#c98a62 45%,#eae6e2)"></div>
      <h2 class="post-card__title">Lorem ipsum dolor sit amet</h2>
      <p class="post-card__excerpt">Ut consequat, sapien at scelerisque laoreet, nulla turpis aliquet quam, quis imperdiet nulla nisl</p>
      <a class="read-more" href="#">Read More<svg width="34" height="12" viewBox="0 0 34 12"><line x1="8" y1="6" x2="34" y2="6" stroke="#f2665c" stroke-width="0.8"/><circle cx="6" cy="6" r="5.5" fill="#f2665c"/><path d="M3.8 6h4.4M6 3.8v4.4" stroke="#fff" stroke-width="1.1"/></svg></a>
    </article>
  </main>

  <nav class="pagination">
    <p class="pagination__count">Showing&nbsp; 1 - 6</p>
    <div class="pagination__pages">
      <span class="current">1</span>
      <span>2</span>
      <svg width="9" height="8" viewBox="0 0 9 8"><path d="M1 1l3 3-3 3M5 1l3 3-3 3" fill="none" stroke="#2c2c2c" stroke-width="0.9"/></svg>
    </div>
  </nav>

  <footer class="site-footer">
    <div class="footer-brand">TARNWISP</div>
    <div class="footer-col" style="left:274px">
      <h3>COMPANY</h3>
      <ul><li>Terms of Use</li><li>Privacy Policy</li><li>Editorial Policy</li><li>How We Make Money</li></ul>
    </div>
    <div class="footer-col" style="left:424px">
      <h3>DISCOVER</h3>
      <ul><li>Terms of Use</li><li>Privacy Policy</li><li>Editorial Policy</li><li>How We Make Money</li></ul>
    </div>
    <div class="footer-col" style="left:556px">
      <h3>ABOUT</h3>
      <ul><li>About</li><li>Contact</li><li>Media</li></ul>
    </div>
    <div class="footer-col" style="left:665px">
      <h3>CONTACT INFO</h3>
      <ul>
        <li><svg width="8" height="10" viewBox="0 0 8 10"><path d="M4 0a4 4 0 0 1 4 4c0 3-4 6-4 6S0 7 0 4a4 4 0 0 1 4-4z" fill="#f2665c"/><circle cx="4" cy="4" r="1.5" fill="#252626"/></svg>48 Alder Lane N.W, Suite 210</li>
        <li><svg width="8" height="10" viewBox="0 0 8 10"><path d="M1.5 1l2 .3.4 2.2-1.1.8a6 6 0 0 0 2.2 2.6l.9-1 2 .6.1 2c-4.4.3-7.4-4.1-6.5-7.5z" fill="#f2665c"/></svg>01 555 284 917</li>
        <li><svg width="9" height="7" viewBox="0 0 9 7"><rect width="9" height="7" rx="0.8" fill="#f2665c"/><path d="M0.5 0.8l4 3 4-3" fill="none" stroke="#252626" stroke-width="0.8"/></svg>hello@tarnwisp.com</li>
        <li class="social">Social <span class="dot" aria-label="Social profile"></span><span class="dot" aria-label="Social profile"></span><span class="dot" aria-label="Social profile"></span></li>
      </ul>
    </div>
    <p class="copyright">© 2021 <strong>TarnWisp</strong>. All right reserved</p>
  </footer>
</body>
</html>
```